Plakate für Psychologische Beratung am Telefon
Zielgruppe
Psychologische Beratung am Telefon
Aufgabenstellung
anliegendes Word Dokument soll als eine Art 'Plakat' (pdf Datei) erstellt werden. Diese PDF Datei wird dann an alle MitarbeiterInnen gesandt und soll Auskunft über das Beratungsangebot geben. Die Farben bitte so wie auf dieser Website (das ist unser Mutterunternehmen). www.lernwerk-kolleg.example.

```html
<!DOCTYPE html>
<html lang="de">
<head>
<meta charset="utf-8">
<title>Beratungs-Telefon – Plakat</title>
<link rel="stylesheet" href="https://fonts.googleapis.com/css2?family=Open+Sans:wght@400;600;700&display=swap">
<style>
:root{
  --blue:#3f6499;
  --blue-dark:#2f4f80;
  --ink:#1f1f24;
  --bg-top:#d9e4f4;
  --bg-light:#f4f7fc;
  --white:#ffffff;
}
*{margin:0;padding:0;box-sizing:border-box}
html,body{width:811px;height:1200px;overflow:hidden;background:#fff}
body{font-family:"Open Sans",Arial,sans-serif;color:var(--ink)}
.poster{position:relative;width:811px;height:1200px;overflow:hidden;
  background:linear-gradient(160deg,var(--bg-top) 0%,var(--bg-light) 35%,#e6edf8 70%,#d4e0f2 100%)}
.brand{position:absolute;left:470px;top:62px;display:flex;align-items:center;gap:10px;
  font-size:19px;font-weight:600;letter-spacing:2px;color:var(--ink)}
.brand-square{width:18px;height:18px;background:var(--blue)}
.headline{position:absolute;left:40px;top:128px;font-size:31px;line-height:43px;text-transform:uppercase;letter-spacing:.2px}
.headline .light{font-weight:400}
.headline .bold{font-weight:700}
.band{position:absolute;left:0;top:330px;width:811px;height:9px;background:var(--blue)}
.hotline{position:absolute;left:0;top:330px;width:393px;height:220px;background:var(--blue);color:var(--white);
  padding:28px 0 0 31px;box-shadow:2px 3px 5px rgba(0,0,0,.25)}
.hotline .intro{font-size:16.5px;font-weight:700;line-height:29px}
.hotline .phone{font-size:28px;font-weight:700;line-height:38px}
.hotline .note{font-size:16.5px;font-weight:600;line-height:29px}
.hotline .hours{font-size:16.5px;font-weight:400;line-height:30px}
.photo{position:absolute;left:395px;top:339px;width:416px;height:346px;
  background:radial-gradient(circle at 45% 40%,#c9a88f 0%,#9aa6b3 35%,#cfd6de 65%,rgba(240,244,250,0) 100%),
  linear-gradient(180deg,#aeb7c2,#e9eef5)}
.rule{position:absolute;left:71px;top:550px;width:8px;height:610px;background:var(--blue)}
.panel{position:absolute;left:79px;top:643px;width:703px;height:405px;background:rgba(255,255,255,.85);
  box-shadow:1px 2px 4px rgba(0,0,0,.2)}
.tab{position:absolute;left:79px;background:var(--blue);color:var(--white);font-weight:700;
  font-size:31px;padding-left:14px;box-shadow:2px 3px 4px rgba(0,0,0,.25);display:flex;align-items:center}
.tab-who{top:593px;width:204px;height:54px}
.tab-fields{top:685px;width:406px;height:55px}
.tab-process{top:886px;width:232px;height:47px}
.who-text{position:absolute;left:95px;top:653px;font-size:14px}
.field{position:absolute;top:746px;font-size:14.2px;line-height:20.5px}
.field b{font-weight:700}
.field-private{left:95px;width:220px}
.field-mental{left:314px;width:200px}
.field-work{left:517px;width:260px}
.process{position:absolute;left:99px;top:947px;font-size:14.2px;line-height:20.5px}
.process .lead{font-size:17px;font-weight:700;margin-bottom:1px}
.process ul{list-style:none}
.process li{position:relative;padding-left:25px}
.process li::before{content:"•";position:absolute;left:0}
.anon{position:absolute;left:99px;top:1079px;font-size:14.2px;line-height:20px;font-weight:600}
</style>
</head>
<body>
<main class="poster">
  <div class="brand"><span class="brand-square"></span>LERNWERK KOLLEG</div>

  <h1 class="headline">
    <span class="light">Das anonyme</span><br>
    <span class="bold">Beratungs- und Begleitangebot</span><br>
    <span class="bold">für Mitarbeiterinnen &amp; Führungskräfte</span><br>
    <span class="light">in&nbsp; schwierigen Berufs- und Lebensphasen.</span>
  </h1>

  <div class="band"></div>

  <section class="hotline">
    <p class="intro">Das LWK Beratungs-Telefon des LWK<br>Lernwerk Kolleg für Weiterbildung.</p>
    <p class="phone">Tel.: 0451 – 555 20 – 140</p>
    <p class="note">Sofortberatung oder Terminvereinbarung<br>zu Ihrer Wunschzeit</p>
    <p class="hours">Di. 14:00 – 17:00 Uhr &amp; Do. 9:00 – 12:00 Uhr</p>
  </section>

  <div class="photo" role="img" aria-label="Foto einer lächelnden Beraterin mit Headset am Arbeitsplatz"></div>

  <div class="rule"></div>
  <div class="panel"></div>

  <h2 class="tab tab-who">FÜR WEN?</h2>
  <p class="who-text">Für alle Mitarbeitenden und Führungskräfte der LW|K.</p>

  <h2 class="tab tab-fields">DIE BERATUNGSFELDER</h2>
  <p class="field field-private"><b>Private Anliegen:</b><br>Partnerschaftskonflikte,<br>Erziehungsberatung,<br>Trennung/Scheidung, Verlust,<br>Trauer, Todesfall,<br>Schockdiagnosen usw.</p>
  <p class="field field-mental"><b>Psychische Gesundheit:</b><br>Sucht und Abhängigkeiten,<br>Depressionen, Burnout,<br>Ängste usw.</p>
  <p class="field field-work"><b>Berufliche Anliegen:</b><br>Vereinbarkeit Beruf und Familie,<br>Konflikte mit Kolleginnen oder<br>Kollegen oder Vorgesetzten,<br>Überforderungen am Arbeitsplatz<br>sowie Coaching für Führungskräfte</p>

  <h2 class="tab tab-process">DER ABLAUF</h2>
  <div class="process">
    <p class="lead">Sie wählen 0451 555 20 140</p>
    <ul>
      <li>Ihr Anruf wird von den psychologischen Assistentinnen angenommen</li>
      <li>Diese erfragen ein Stichwort zu Ihrem Anliegen, um Sie</li>
      <li>direkt mit einer Expertin oder einem Experten für Ihr Thema verbinden zu können</li>
    </ul>
  </div>

  <p class="anon">Anonymität<br>Die Beratung ist anonym. Sie müssen Ihren Namen nicht nennen.<br>Unsere Beraterinnen und Berater verfügen alle über langjährige Beratungserfahrung<br>und je nach Thema auch über eine Psychotherapiezulassung.</p>
</main>
</body>
</html>
```